Kelmora Legal Business Card

I require a corporate business card for a new legal services business.

I do not have a logo, nor do I want one.

I require a clean, neat a professional card for a law firm.

Details:

Business Name: Kelmora Legal
Name: Debra Lindqvist
Title: Corporate Services Manager
Location: Office 14 (Top Floor), Toravel Business Centre, Quinlan Grove Street, Alotau CBD, Milne Bay Province.
Postal Address: PO Box 593, Alotau, 211, Milne Bay Province, Papua New Guinea.
Contact: T: +675 6418250, F: +675 6413362, M: +675 72915867, E: dlindqvist@kelmoraexample.com.pg.

I look forward to your design submissions.

Industry/Entity Type

Legal

```html
<!DOCTYPE html>
<html lang="en">
<head>
<meta charset="UTF-8">
<title>Kelmora Legal Business Card</title>
<link href="https://fonts.googleapis.com/css2?family=Arimo:wght@400;700&family=Tinos:wght@700&display=swap" rel="stylesheet">
<style>
  :root {
    --backdrop: #1d1d1e;
    --card-light: #fbfbfb;
    --card-mid: #e6e6e7;
    --card-edge: #cfcfd1;
    --ink: #2b2b2d;
    --ink-soft: #3a3a3c;
    --name-grey: #8a8d94;
    --accent-bar: #9a9ca2;
    --logo-ink: #3c3c3e;
    --band: #444446;
  }
  * { box-sizing: border-box; margin: 0; padding: 0; }
  html, body {
    width: 1200px; height: 908px; overflow: hidden;
    background: var(--backdrop);
  }
  .canvas { position: relative; width: 1200px; height: 908px; }
  .card {
    position: absolute; left: 290px;
    width: 620px; height: 354px;
    border-radius: 24px;
    overflow: hidden;
    background: radial-gradient(ellipse at 55% 35%, var(--card-light) 0%, var(--card-mid) 70%, var(--card-edge) 100%);
  }
  .card--back { top: 80px; }
  .card--front { top: 474px; }

  .brand {
    font-family: "Tinos", "Times New Roman", serif;
    font-weight: 700;
    color: var(--logo-ink);
    letter-spacing: 0.5px;
    white-space: nowrap;
  }
  .card--back .brand {
    position: absolute; left: 0; right: 0; top: 148px;
    text-align: center; font-size: 50px;
  }
  .card--front .brand {
    position: absolute; left: 318px; top: 62px;
    font-size: 40px;
  }

  .identity {
    position: absolute; left: 34px; top: 56px;
    padding-left: 14px;
    border-left: 4px solid var(--accent-bar);
    font-family: "Arimo", Arial, sans-serif;
    text-transform: uppercase;
  }
  .identity__name {
    font-size: 19px; font-weight: 700; color: var(--name-grey);
    letter-spacing: 0.5px; line-height: 24px;
  }
  .identity__title {
    font-size: 13px; color: var(--name-grey); line-height: 18px;
  }

  .contact, .address {
    position: absolute; left: 40px;
    font-family: "Arimo", Arial, sans-serif;
    color: var(--ink-soft); font-size: 13px; line-height: 16px;
    white-space: nowrap;
  }
  .contact { top: 140px; }
  .contact__phone { font-weight: 700; color: var(--ink); }
  .address { top: 210px; }
  .card__band {
    position: absolute; left: 0; right: 0; bottom: 0; height: 48px;
    background: var(--band);
  }
</style>
</head>
<body>
<main class="canvas">
  <section class="card card--back">
    <p class="brand">Kelmora Legal</p>
  </section>

  <section class="card card--front">
    <div class="identity">
      <p class="identity__name">Debra Lindqvist</p>
      <p class="identity__title">Corporate Services Manager</p>
    </div>
    <p class="brand">Kelmora Legal</p>
    <div class="contact">
      <p class="contact__phone">T: +675 6418250 &nbsp; F: +675 6413362</p>
      <p class="contact__phone">M: +675 72915867</p>
      <p>E: dlindqvist@kelmoraexample.com.pg</p>
    </div>
    <div class="address">
      <p>Office 14 (Top Floor), Toravel Business Centre,</p>
      <p>Quinlan Grove Street, Alotau CBD, Milne Bay Province</p>
      <p>PO Box 593, Alotau, 211, Milne Bay Province,</p>
      <p>Papua New Guinea</p>
    </div>
    <div class="card__band"></div>
  </section>
</main>
</body>
</html>
```